Business card design needed

Family General Practitioner/ Family Physician.
Logo is the logo of the Crestmoor Guild of Family Clinicians Australia
http://kvplm.tarevo.edu.au/PictureGallery/logos/pages/CGFC%20logo_jpg.htm

Reason: Just a bit more time to make changes and the weekend for me to look at things closely and to choose. Thanks, Lumi

Thanks for all the submissions. So many of them are really works of art. Not one of them are not good. The ones that I am eliminating are the ones that I think are not suitable for me personally only, and because if I don't, it makes it very difficult to decide as many of you are also sending me slight variations of a card. I have just decided to choose a second place card too. Can't thank you all enough. Good luck, Lumi. P.S - Working today till 10 pm as the card says :-), so probably won't be able to give a feedback till late Saturday night or Sunday morning here in Sydney, Australia. 

Reason: Just added a second place to the budget and realised that Australia is ahead of the rest of the world in the time zone (only :-) - don't want to offend anyone or start a debate!! ) , so Monday deadline will mean it will be a weekend for the rest of the world. Just wanted to give everyone more time to submit their best, especially since I will be picking a second card too. Can't thank everyone enough for the submissions. P.S - Not keen on photos on the card.

Contact Information for Business Card

Dr. Lumi Harcourt M.B.B.S., F.C.G.F.C
Family General Practitioner
Address, timings, phone and fax number on the back.

Requirements
Must have
• Timings
Mon 7 am - 7 pm
Tues 7 am - 12 pm
Wed 7 am - 10 pm
Thurs 7 am - 12 pm
Fri 7 am - 8 pm
Sat 8 am - 10 pm
Sun - Off

```html
<!DOCTYPE html>
<html lang="en">
<head>
<meta charset="utf-8">
<title>Dr. Lumi Harcourt – Business Card</title>
<link rel="stylesheet" href="https://fonts.googleapis.com/css2?family=Noto+Sans:wght@400;700&display=swap">
<style>
  :root {
    --brand-red: #c1202b;
    --ink: #111111;
    --paper: #ffffff;
    --card-edge: #555555;
  }
  html, body {
    margin: 0;
    padding: 0;
    width: 1200px;
    height: 1017px;
    overflow: hidden;
    background: var(--paper);
  }
  .sheet {
    display: block;
    width: 1200px;
    height: 1017px;
    font-family: "Noto Sans", Verdana, sans-serif;
  }
  .card-outline { fill: var(--paper); stroke: var(--card-edge); stroke-width: 1; }
  .side-label { fill: var(--ink); font-size: 26px; }
  .red-fill { fill: var(--brand-red); }
  .guild-name { fill: var(--brand-red); font-size: 38px; font-weight: 700; }
  .doctor-surname { fill: var(--brand-red); font-size: 50px; font-weight: 700; }
  .doctor-given { fill: var(--brand-red); font-size: 47px; font-weight: 400; }
  .credentials { fill: var(--ink); font-size: 31px; }
  .role { fill: var(--ink); font-size: 26px; }
  .address { fill: var(--brand-red); font-size: 24px; }
  .contact { fill: var(--brand-red); font-size: 28px; }
  .contact-key { font-weight: 700; }
  .hours-title { fill: var(--brand-red); font-size: 27px; font-weight: 700; }
  .time-tag-text { fill: var(--paper); font-size: 22px; font-weight: 700; text-anchor: middle; }
  .time-rail { stroke: var(--brand-red); stroke-width: 3; fill: none; }
  .column-divider { stroke: var(--paper); stroke-width: 2; }
  .chart-frame { fill: none; stroke: var(--brand-red); stroke-width: 3; }
  .day-letter { fill: var(--paper); font-size: 22px; font-weight: 700; text-anchor: middle; }
  .closed-note { fill: var(--brand-red); font-size: 26px; font-weight: 700; text-anchor: middle; }
</style>
</head>
<body>
<svg class="sheet" viewBox="0 0 1100 934" preserveAspectRatio="none" xmlns="http://www.w3.org/2000/svg">
  <!-- Front side -->
  <text class="side-label" x="95" y="191">Front</text>
  <g class="card card-front">
    <rect class="card-outline" x="304.5" y="2.5" width="795" height="459"/>
    <g class="guild-mark">
      <rect class="red-fill" x="352" y="40" width="70" height="70"/>
      <text class="guild-name" x="352" y="170">CGFC</text>
    </g>
    <text x="535" y="89"><tspan class="doctor-surname">Dr. Harcourt,</tspan><tspan class="doctor-given"> Lumi</tspan></text>
    <text class="credentials" x="537" y="131">M.B.B.S., F.C.G.F.C</text>
    <text class="role" x="537" y="164">Family General Practitioner</text>
    <g class="address">
      <text x="352" y="338">Upper Level, Linden Court,</text>
      <text x="352" y="368">Marlow Heights Shopping Centre</text>
      <text x="352" y="397">Marlow Hill, NSW 2199</text>
    </g>
    <g class="contact">
      <text x="815" y="340"><tspan class="contact-key">P:</tspan> 02 5550 1400</text>
      <text x="815" y="375"><tspan class="contact-key">F:</tspan> 02 5550 1233</text>
    </g>
  </g>

  <!-- Back side -->
  <text class="side-label" x="108" y="690">Back</text>
  <g class="card card-back">
    <rect class="card-outline" x="304.5" y="472.5" width="795" height="459"/>
    <text class="hours-title" x="352" y="513">Working Hours</text>

    <g class="time-scale">
      <path class="time-rail" d="M450 544 H477 M450 600 H477 M450 657 H477 M450 713 H477 M450 769 H477 M450 825 H477 M450 881 H477 M477 544 V881"/>
      <g class="red-fill">
        <rect x="352" y="527" width="98" height="34"/>
        <rect x="352" y="583" width="98" height="34"/>
        <rect x="352" y="640" width="98" height="34"/>
        <rect x="352" y="696" width="98" height="34"/>
        <rect x="352" y="752" width="98" height="34"/>
        <rect x="352" y="808" width="98" height="34"/>
        <rect x="352" y="864" width="98" height="34"/>
      </g>
      <text class="time-tag-text" x="401" y="552">7 AM</text>
      <text class="time-tag-text" x="401" y="608">10 AM</text>
      <text class="time-tag-text" x="401" y="665">1 PM</text>
      <text class="time-tag-text" x="401" y="721">6 PM</text>
      <text class="time-tag-text" x="401" y="777">7 PM</text>
      <text class="time-tag-text" x="401" y="833">8 PM</text>
      <text class="time-tag-text" x="401" y="889">10 PM</text>
    </g>

    <g class="hours-chart">
      <g class="red-fill">
        <rect class="day-mon" x="496" y="544" width="85" height="225"/>
        <rect class="day-tue" x="580" y="544" width="85" height="94"/>
        <rect class="day-wed" x="664" y="544" width="85" height="337"/>
        <rect class="day-thu" x="748" y="544" width="85" height="94"/>
        <rect class="day-fri" x="832" y="544" width="85" height="281"/>
        <rect class="day-sat" x="916" y="563" width="85" height="318"/>
      </g>
      <path class="column-divider" d="M580.5 546 V769 M664.5 546 V638 M748.5 546 V638 M832.5 546 V638 M916.5 563 V825"/>
      <rect class="chart-frame" x="496" y="545" width="560" height="336"/>
      <line class="time-rail" x1="1002" y1="545" x2="1002" y2="881"/>

      <text class="day-letter" x="538" y="625">M</text>
      <text class="day-letter" x="538" y="663">O</text>
      <text class="day-letter" x="538" y="701">N</text>

      <text class="day-letter" x="622" y="572">T</text>
      <text class="day-letter" x="622" y="600">U</text>
      <text class="day-letter" x="622" y="628">E</text>

      <text class="day-letter" x="706" y="700">W</text>
      <text class="day-letter" x="706" y="738">E</text>
      <text class="day-letter" x="706" y="776">D</text>

      <text class="day-letter" x="790" y="572">T</text>
      <text class="day-letter" x="790" y="600">H</text>
      <text class="day-letter" x="790" y="628">U</text>

      <text class="day-letter" x="874" y="660">F</text>
      <text class="day-letter" x="874" y="698">R</text>
      <text class="day-letter" x="874" y="736">I</text>

      <text class="day-letter" x="958" y="700">S</text>
      <text class="day-letter" x="958" y="738">A</text>
      <text class="day-letter" x="958" y="776">T</text>

      <text class="closed-note" transform="translate(1037 714) rotate(-90)">Sunday closed</text>
    </g>
  </g>
</svg>
</body>
</html>
```